Calloway Ridge Associates Stationery

Use attached logo for stationery
Stationery, Letterhead and Envelope + Business cards

Tag line: Walking alongside those doing the work of the Gospel

```html
<!DOCTYPE html>
<html lang="en">
<head>
<meta charset="utf-8">
<title>Calloway Ridge Associates Stationery</title>
<link href="https://fonts.googleapis.com/css2?family=Montserrat:wght@500;600&family=Roboto:wght@400&display=swap" rel="stylesheet">
<style>
  :root{
    --bg:#e8e9eb;
    --paper:#f4f5f4;
    --navy:#0d3a7d;
    --gold:#e7b51f;
    --sky:#5bbfe6;
    --ink:#2a2f36;
    --rule:#c9ccd1;
  }
  *{box-sizing:border-box;margin:0;padding:0}
  html,body{width:1200px;height:792px;overflow:hidden;background:var(--bg)}
  body{position:relative;font-family:"Roboto",Arial,sans-serif;color:var(--ink)}
  .sheet{position:absolute;background:var(--paper);box-shadow:0 3px 10px rgba(0,0,0,.18)}
  .brand{font-family:"Montserrat",Arial,sans-serif;font-weight:600;color:var(--navy);text-align:center;line-height:1.15;letter-spacing:.04em;text-transform:uppercase}

  /* business card front */
  .card-front{left:166px;top:72px;width:158px;height:90px;background:var(--navy);display:flex;align-items:center;justify-content:center}
  .card-front .brand{color:#fff;font-size:9px;width:120px}

  /* business card back */
  .card-back{left:166px;top:182px;width:158px;height:90px}
  .card-back .frame{position:absolute;inset:6px;border:1px solid var(--gold)}
  .card-back .brand{position:absolute;right:12px;top:11px;font-size:4px;width:40px;text-align:right}
  .card-back .person{position:absolute;left:0;right:0;top:30px;text-align:center;font-family:"Montserrat",Arial,sans-serif;font-weight:500;font-size:11px;letter-spacing:.14em;color:var(--navy)}
  .card-back .role{position:absolute;left:0;right:0;top:45px;text-align:center;font-size:3.6px;letter-spacing:.35em;color:var(--sky);text-transform:uppercase}
  .card-back .contact{position:absolute;left:32px;right:32px;top:60px;font-size:3.4px;color:#555;text-align:center;border-top:.5px solid var(--rule)}
  .card-back .contact p{padding:2px 0;border-bottom:.5px solid var(--rule)}
  .card-back .contact .row{display:flex;justify-content:space-around}

  /* letterhead */
  .letterhead{left:372px;top:104px;width:294px;height:416px}
  .letterhead .frame{position:absolute;left:14px;top:14px;right:14px;bottom:14px;border:1.2px solid var(--gold)}
  .letterhead .brand.head{position:absolute;right:42px;top:40px;font-size:5.5px;width:60px}
  .letterhead .watermark{position:absolute;left:24px;right:24px;top:232px;font-family:"Montserrat",Arial,sans-serif;font-weight:600;font-size:24px;text-align:center;color:rgba(13,58,125,.12);letter-spacing:.04em;text-transform:uppercase;line-height:1.1}
  .letterhead .body{position:absolute;left:45px;right:37px;top:104px;font-size:5px;line-height:1.75;color:#222}
  .letterhead .body p{margin-bottom:6px}
  .letterhead .signature{display:block;width:58px;height:12px;margin-top:2px;background:linear-gradient(90deg,rgba(214,58,58,.55),rgba(214,58,58,.15))}

  /* envelope (front, address side) */
  .envelope-top{left:720px;top:72px;width:330px;height:164px}
  .envelope-top .brand{position:absolute;left:18px;top:40px;font-size:7px;width:66px}
  .envelope-top .address{position:absolute;left:106px;top:120px;width:120px;font-size:4.2px;color:#555;text-align:center;border-top:.5px solid var(--rule)}
  .envelope-top .address p{padding:2.5px 0;border-bottom:.5px solid var(--rule)}
  .envelope-top .address .row{display:flex}
  .envelope-top .address .row span{flex:1}
  .envelope-top .address .row span+span{border-left:.5px solid var(--rule)}

  /* folder */
  .folder{left:720px;top:253px;width:332px;height:439px}
  .folder .band{position:absolute;left:0;right:0;height:18px;background:var(--navy)}
  .folder .band.top{top:0;border-radius:4px 4px 0 0}
  .folder .band.bottom{bottom:0;border-radius:0 0 4px 4px}
  .folder .brand{position:absolute;left:10px;top:82px;width:130px;font-size:14px}
  .folder .tagline-rule{position:absolute;left:10px;top:126px;width:130px;height:1px;background:var(--sky)}

  /* envelope (flap side) */
  .envelope-back{left:338px;top:550px;width:330px;height:165px;overflow:hidden}
  .envelope-back .flap{position:absolute;left:0;right:0;top:0;height:42px;background:var(--navy);border-radius:10px 10px 0 0;display:flex;align-items:center;justify-content:center}
  .envelope-back .flap .brand{color:#fff;font-size:5px;width:50px}
  .envelope-back .brand.main{position:absolute;left:105px;top:68px;width:120px;font-size:13px}
</style>
</head>
<body>

  <section class="sheet card-front" aria-label="Business card front">
    <div class="brand">Calloway Ridge Associates</div>
  </section>

  <section class="sheet card-back" aria-label="Business card back">
    <div class="frame"></div>
    <div class="brand">Calloway Ridge Associates</div>
    <div class="person">MARLO VENTRICE</div>
    <div class="role">Graphic Designer</div>
    <div class="contact">
      <p>Harbor Lane - Westfield - OR</p>
      <p class="row"><span>+1 503 555 0142</span><span>marlo@callowayridge.org</span></p>
    </div>
  </section>

  <section class="sheet letterhead" aria-label="Letterhead">
    <div class="frame"></div>
    <div class="brand head">Calloway Ridge Associates</div>
    <div class="watermark">Calloway Ridge<br>Associates</div>
    <div class="body">
      <p>Dear Customers,</p>
      <p>Lorem ipsum dolor sit amet, consectetur adipiscing elit. Nunc varius, lectus vel eleifend vulputate, tortor diam sollicitudin mauris, vitae finibus diam est at sem. Aliquam mattis in mauris vel porta. Praesent volutpat lacus non massa sagittis, id eleifend sapien vestibulum. Etiam pretium odio rutrum semper scelerisque. Vestibulum tortor ligula, bibendum non dictum vitae, luctus eget massa.</p>
      <p>Lorem ipsum dolor sit amet, consectetur adipiscing elit. Suspendisse dapibus nunc eu molestie condimentum. Sed quis dolor non lorem lobortis convallis. Sed pretium erat ac tellus dapibus tempus. Maecenas semper erat id dictum tempor. Sed quis urna a orci luctus porta. Nam tempus libero mollis erat gravida, eget ullamcorper tortor commodo.</p>
      <p>Sincerely yours,<span class="signature" role="img" aria-label="Handwritten signature"></span></p>
    </div>
  </section>

  <section class="sheet envelope-top" aria-label="Envelope front">
    <div class="brand">Calloway Ridge Associates</div>
    <div class="address">
      <p>48 Linden St, Westfield, Oregon 97035, USA</p>
      <p class="row"><span>www.callowayridge.org</span><span>hello@callowayridge.org</span></p>
    </div>
  </section>

  <section class="sheet folder" aria-label="Presentation folder">
    <div class="band top"></div>
    <div class="brand">Calloway Ridge Associates</div>
    <div class="band bottom"></div>
  </section>

  <section class="sheet envelope-back" aria-label="Envelope back">
    <div class="flap"><div class="brand">Calloway Ridge Associates</div></div>
    <div class="brand main">Calloway Ridge Associates</div>
  </section>

</body>
</html>
```